Business Card for IT Support Company
Aide Nova
Business Card for IT Support Company - Information Technology
Creative Brief
Professional
Assistance Informatique 24/7
Tél. 0900 417 536
2.50 CHF/min de 8h à 22h et 3.50 CHF/min de 22h à 8h depuis le réseau fixe.
info@aide-nova.ch
http://www.aide-nova.ch
No specific name, this is only a hotline IT support number Business Card (phone number is in the title) in Address box, it's the rates on the Business Number. We will use brivopress . ch as the printing company, here are the exact size in mm they send to me: Business card Size is 85x55mm (But file dimension must be 91x61mm) Colors needs to be send in CMYK, minimum 200 dpi, maximum quality.
- Contrôle à distance PC/MAC - Support technique informatique - Formation / Consulting / Coaching - Infographie / Graphisme - Création de Site Web - Smartphone / Tablette

```html
<!DOCTYPE html>
<html lang="fr">
<head>
<meta charset="utf-8">
<title>Aide Nova – Carte de visite</title>
<link rel="stylesheet" href="https://fonts.googleapis.com/css2?family=Open+Sans:wght@400;600&display=swap">
<style>
  :root {
    --page-bg: #d9d6d2;
    --card-clear: rgba(255, 255, 255, 0.55);
    --card-edge: rgba(255, 255, 255, 0.9);
    --band-dark: #2b2b2d;
    --band-light: #4a4a4d;
    --brand-red: #d8232a;
    --ink-dark: #2a2a2a;
    --ink-light: #f4f4f4;
  }
  * { box-sizing: border-box; margin: 0; padding: 0; }
  html, body { width: 1200px; height: 545px; overflow: hidden; }
  body {
    background: var(--page-bg);
    font-family: "Open Sans", Arial, sans-serif;
    position: relative;
  }
  .business-card {
    position: absolute;
    top: 122px;
    width: 450px;
    height: 302px;
    background: var(--card-clear);
    border: 1px solid var(--card-edge);
    border-radius: 4px;
    box-shadow: 0 6px 18px rgba(0, 0, 0, 0.12);
    overflow: hidden;
  }
  .card-front { left: 84px; }
  .card-back { left: 666px; }

  .brand {
    position: absolute;
    top: 38px;
    display: flex;
    align-items: center;
    gap: 14px;
  }
  .card-front .brand { left: 108px; }
  .card-back .brand {
    left: 108px;
    transform: scaleX(-1);
    opacity: 0.55;
  }
  .brand-dot {
    width: 54px;
    height: 54px;
    border-radius: 50%;
    background: var(--brand-red);
  }
  .brand-name {
    font-size: 30px;
    font-weight: 600;
    color: var(--ink-dark);
    letter-spacing: 0.5px;
  }

  .dark-band {
    position: absolute;
    left: 0;
    right: 0;
    background: linear-gradient(180deg, var(--band-light), var(--band-dark) 45%);
  }
  .card-front .dark-band { top: 128px; height: 108px; }
  .card-back .dark-band {
    top: 118px;
    height: 128px;
    display: flex;
    flex-direction: column;
    justify-content: center;
    gap: 8px;
    text-align: center;
    color: var(--ink-light);
    font-size: 12.5px;
    letter-spacing: 0.2px;
  }

  .contact-list {
    display: flex;
    justify-content: space-around;
    height: 100%;
    padding: 16px 10px 0;
    list-style: none;
  }
  .contact-item {
    display: flex;
    flex-direction: column;
    align-items: center;
    gap: 14px;
    width: 33%;
  }
  .contact-icon { width: 44px; height: 44px; }
  .contact-text {
    font-size: 9.5px;
    letter-spacing: 1.2px;
    color: var(--ink-light);
    text-transform: uppercase;
    white-space: nowrap;
  }
  .contact-phone { font-size: 12px; letter-spacing: 2px; }
</style>
</head>
<body>
  <section class="business-card card-front" aria-label="Recto de la carte">
    <div class="brand">
      <span class="brand-dot"></span>
      <span class="brand-name">Aide Nova</span>
    </div>
    <div class="dark-band">
      <ul class="contact-list">
        <li class="contact-item">
          <svg class="contact-icon" viewBox="0 0 44 44" aria-hidden="true">
            <circle cx="22" cy="22" r="20" fill="var(--brand-red)"/>
            <rect x="12" y="15" width="20" height="14" rx="1.5" fill="none" stroke="#fff" stroke-width="2"/>
            <path d="M12.5 16 L22 23 L31.5 16" fill="none" stroke="#fff" stroke-width="2"/>
          </svg>
          <span class="contact-text">info@aide-nova.ch</span>
        </li>
        <li class="contact-item">
          <svg class="contact-icon" viewBox="0 0 44 44" aria-hidden="true">
            <circle cx="22" cy="22" r="20" fill="var(--brand-red)"/>
            <circle cx="22" cy="22" r="10" fill="none" stroke="#fff" stroke-width="2"/>
            <ellipse cx="22" cy="22" rx="4.5" ry="10" fill="none" stroke="#fff" stroke-width="1.6"/>
            <path d="M12 22 H32" stroke="#fff" stroke-width="1.6"/>
          </svg>
          <span class="contact-text">www.aide-nova.ch</span>
        </li>
        <li class="contact-item">
          <svg class="contact-icon" viewBox="0 0 44 44" aria-hidden="true">
            <circle cx="22" cy="22" r="20" fill="var(--brand-red)"/>
            <rect x="16" y="11" width="12" height="22" rx="2" fill="none" stroke="#fff" stroke-width="2"/>
            <circle cx="22" cy="29" r="1.3" fill="#fff"/>
          </svg>
          <span class="contact-text contact-phone">0900 417 536</span>
        </li>
      </ul>
    </div>
  </section>

  <section class="business-card card-back" aria-label="Verso de la carte">
    <div class="brand" aria-hidden="true">
      <span class="brand-dot"></span>
      <span class="brand-name">Aide Nova</span>
    </div>
    <div class="dark-band">
      <p class="service-line">Contrôle à distance PC/MAC | Support technique informatique</p>
      <p class="service-line">Formation / Consulting / Coaching | Infographie / Graphisme</p>
      <p class="service-line">Création de Site Web | Smartphone / Tablette</p>
    </div>
  </section>
</body>
</html>
```